Fun Trendy High End Spa Services
Business Card, Gift Certificate, Gift Certificate Envelope
I need double sided standard sized Business Card [3.5" x 2"]
We like what is in logo that was uploaded but please use your creativity. We are open to any ideas.
Simple
Lena Harbus LMT
Owner
Mobile
BP@BrightPebblo.com
BrightPebblo.com
We are open to all concepts. So please be creative. This is for Very high end spa service so it needs to look very good. We thought black paper for a base on business cards, gift certificate and GC envelope but are open to any and all ideas! Thank You! We will pick a winner early if we find the perfect design.
"The greatest wealth is health"
(Doesnt need " " on there just use your own idea and play with it.)
Here is The winning logo design. We really like the style but please feel free to be creative with it! Thank you so much!
This is the style of gift certificate that we want designed to match our business card.

```html
<!DOCTYPE html>
<html lang="en">
<head>
<meta charset="utf-8">
<title>Bright Pebblo – Stationery Set</title>
<link rel="stylesheet" href="https://fonts.googleapis.com/css2?family=Cormorant+Garamond:wght@400;500&family=Tinos:wght@400;700&display=swap">
<style>
  :root{
    --page:#ffffff;
    --ink:#0d0d0d;
    --card:#141414;
    --silver-1:#eeeeee;
    --silver-2:#a9a9a9;
    --silver-3:#d6d6d6;
    --text-light:#e4e4e4;
    --text-mid:#b9b9b9;
    --text-dark:#1a1a1a;
  }
  *{box-sizing:border-box;margin:0;padding:0}
  html,body{width:1200px;height:799px;overflow:hidden;background:var(--page)}
  body{position:relative;font-family:"Tinos",serif;color:var(--text-light)}
  .piece{position:absolute;background:var(--card);overflow:hidden;box-shadow:0 2px 6px rgba(0,0,0,.25)}
  .silver{background:linear-gradient(180deg,var(--silver-1) 0%,var(--silver-2) 45%,var(--silver-3) 70%,var(--silver-2) 100%)}
  .brand{font-family:"Tinos",serif;color:var(--text-light);font-weight:400;white-space:nowrap;display:flex;align-items:center;gap:10px}
  .brand .dot{width:14px;height:14px;border-radius:50%;background:var(--text-light);display:inline-block}

  /* Gift certificate */
  .gift{left:137px;top:144px;width:590px;height:379px}
  .gift .head{position:absolute;left:0;top:0;width:100%;height:126px}
  .gift .head .brand{position:absolute;left:150px;top:38px;font-size:40px}
  .gift .meta{position:absolute;left:470px;top:58px;font-size:13px;color:var(--text-mid);line-height:20px;white-space:nowrap}
  .gift .meta span{display:inline-block;width:66px;border-bottom:1px solid #555;margin-left:6px}
  .gift .band{position:absolute;left:0;top:126px;width:100%;height:220px}
  .gift .title{position:absolute;left:0;width:100%;top:22px;text-align:center;font-size:27px;color:var(--text-dark);letter-spacing:1px;font-variant:small-caps}
  .gift .rule{position:absolute;left:60px;right:60px;top:62px;height:2px;background:var(--text-dark)}
  .gift .field{position:absolute;left:66px;width:420px;font-size:16px;color:var(--text-dark);font-variant:small-caps;display:flex;align-items:flex-end;gap:8px;white-space:nowrap}
  .gift .field i{flex:1;border-bottom:2px solid var(--text-dark);height:14px}
  .gift .field small{font-size:11px}
  .gift .foot{position:absolute;left:0;bottom:0;width:100%;height:33px;display:flex;justify-content:space-around;align-items:center;font-size:11px;color:var(--text-mid)}
  .icon{display:inline-block;width:11px;height:9px;background:var(--text-mid);margin-right:6px;vertical-align:middle}

  /* Cards */
  .card{width:348px;height:198px}
  .card.small{width:283px;height:161px}
  .luxury{position:absolute;font-family:"Cormorant Garamond",serif;color:var(--text-mid);font-size:26px;line-height:1.05;white-space:nowrap}
  .luxury b{font-weight:500;color:var(--text-light);font-size:30px}
  .owner{position:absolute;text-align:center;font-size:15px;color:var(--text-light);white-space:nowrap}
  .owner small{display:block;font-size:10px;color:var(--text-mid)}
  .contacts{position:absolute;font-size:10px;color:var(--text-mid);line-height:16px;text-align:right;white-space:nowrap}
  .strip{position:absolute;left:0;bottom:0;width:100%;height:24px;text-align:center;font-size:10px;color:var(--text-dark);line-height:26px}
  .strip.thin{height:10px}

  .mark{position:absolute;left:986px;top:712px;font-size:30px;color:var(--ink);display:flex;align-items:center;gap:10px;white-space:nowrap;font-family:"Tinos",serif}
  .mark .dot{width:20px;height:20px;border-radius:50%;background:var(--ink)}
</style>
</head>
<body>

<section class="piece gift" aria-label="Gift certificate">
  <div class="head">
    <div class="brand"><span class="dot"></span>Bright Pebblo</div>
    <div class="meta">No:<span></span><br>Date:<span></span></div>
  </div>
  <div class="band silver" role="img" aria-label="Silver band with faint repeating pattern">
    <h1 class="title">Gift Certificate</h1>
    <div class="rule"></div>
    <div class="field" style="top:92px">In The Amount Of: <i></i><small>Dollars $</small></div>
    <div class="field" style="top:124px">A Gift For: <i></i></div>
    <div class="field" style="top:156px">Presented By: <i></i></div>
  </div>
  <div class="foot">
    <span><span class="icon"></span>BP@BrightPebblo.com</span>
    <span><span class="icon"></span>(555) 014-2290</span>
    <span><span class="icon"></span>www.BrightPebblo.com</span>
  </div>
</section>

<section class="piece card" style="left:732px;top:72px" aria-label="Business card back">
  <p class="luxury" style="left:108px;top:86px"><b>Luxury</b> In Home<br><b>Spa</b> Experience</p>
</section>

<section class="piece card" style="left:732px;top:281px" aria-label="Business card front">
  <div class="brand" style="position:absolute;left:20px;top:42px;font-size:26px"><span class="dot"></span>Bright Pebblo</div>
  <div class="owner" style="left:200px;top:36px">Lena Harbus LMT<small>Owner</small></div>
  <div class="contacts" style="right:20px;top:118px">(555) 014-2290<br>BP@BrightPebblo.com<br>Bright_Pebblo</div>
  <div class="strip silver">www.BrightPebblo.com</div>
</section>

<section class="piece card" style="left:732px;top:492px" aria-label="Business card back">
  <p class="luxury" style="left:108px;top:86px"><b>Luxury</b> In Home<br><b>Spa</b> Experience</p>
</section>

<section class="piece card small" style="left:137px;top:535px" aria-label="Business card back">
  <p class="luxury" style="left:14px;top:22px;font-size:21px"><b style="font-size:25px">Luxury</b><br><span style="padding-left:32px">In Home</span><br><b style="font-size:25px">Spa</b> Experience</p>
  <div class="strip silver thin"></div>
</section>

<section class="piece card small" style="left:432px;top:535px" aria-label="Business card front">
  <div class="brand" style="position:absolute;left:14px;top:34px;font-size:19px;gap:7px"><span class="dot" style="width:10px;height:10px"></span>Bright Pebblo</div>
  <div class="owner" style="left:168px;top:26px;font-size:12px">Lena Harbus LMT<small style="font-size:8px">Owner</small></div>
  <div class="contacts" style="right:14px;top:92px;font-size:8px;line-height:13px">(555) 014-2290<br>BP@BrightPebblo.com<br>Bright_Pebblo</div>
  <div class="strip silver" style="height:16px;font-size:8px;line-height:17px">www.BrightPebblo.com</div>
</section>

<div class="mark"><span class="dot"></span>Bright Pebblo</div>

</body>
</html>
```